Creation of a cover for a book on popular ideas (received relief, preconceived ideas).
The picture (either photos or drawings) should represent a or several sheeps in a (French) city. The reason for this is that in France, people following general opinions are pictured as sheeps (following the herd )
Size: 11 x 17.8 cm
AUTHOR: Lucien-Mathis Vorrel
TITLE: Handbook of quiet garden walks
PUBLISHER: Korvane Editions (at the bottom of the page)

General adult public

Book

```html
<!DOCTYPE html>
<html lang="en">
<head>
<meta charset="UTF-8">
<title>Handbook of quiet garden walks — Lucien-Mathis Vorrel</title>
<link rel="stylesheet" href="https://fonts.googleapis.com/css2?family=Prata&family=Jost:wght@400&display=swap">
<style>
  :root {
    --paper: #ffffff;
    --ink: #141414;
  }
  html, body {
    margin: 0;
    padding: 0;
    width: 741px;
    height: 1200px;
    overflow: hidden;
    background: var(--paper);
  }
  .cover {
    position: relative;
    width: 741px;
    height: 1200px;
    background: var(--paper);
    color: var(--ink);
    text-align: center;
  }
  .cover__author {
    position: absolute;
    top: 52px;
    left: 0;
    right: 0;
    margin: 0;
    font-family: "Prata", serif;
    font-weight: 400;
    font-size: 44px;
    line-height: 1;
    letter-spacing: 0.2px;
  }
  .cover__title {
    position: absolute;
    top: 288px;
    left: 0;
    right: 0;
    margin: 0;
    font-family: "Prata", serif;
    font-weight: 400;
    font-size: 78px;
    line-height: 111px;
  }
  .cover__title span { display: block; }
  .cover__publisher {
    position: absolute;
    top: 1082px;
    left: 0;
    right: 0;
    margin: 0;
    font-family: "Jost", sans-serif;
    font-weight: 400;
    font-size: 46px;
    line-height: 1;
  }
</style>
</head>
<body>
  <main class="cover">
    <p class="cover__author">Lucien-Mathis Vorrel</p>
    <h1 class="cover__title">
      <span>Handbook</span>
      <span>of quiet</span>
      <span>garden walks</span>
    </h1>
    <p class="cover__publisher">Korvane Editions</p>
  </main>
</body>
</html>
```